Design Letterhead and Business Card for a travel company

Please refer to the attached document for the details to be included in the letterhead and business cards. Logo and contact details enclosed therein. Client is looking for a professional image.

Please include as many contact details as possible in your entries.

```html
<!DOCTYPE html>
<html lang="en">
<head>
<meta charset="utf-8">
<title>Swiftway Business Card</title>
<link href="https://fonts.googleapis.com/css2?family=Lato:wght@400;700;900&display=swap" rel="stylesheet">
<style>
  :root {
    --bg: #3a3a3a;
    --card: #ffffff;
    --blue: #1a9ad6;
    --purple: #5b2d86;
    --ink: #333333;
    --white: #ffffff;
  }
  * { margin: 0; padding: 0; box-sizing: border-box; }
  html, body { width: 1200px; height: 749px; overflow: hidden; }
  body {
    background: var(--bg);
    font-family: "Lato", Arial, sans-serif;
    position: relative;
  }
  .card {
    position: absolute;
    top: 220px;
    width: 520px;
    height: 300px;
    background: var(--card);
    box-shadow: 0 8px 24px rgba(0,0,0,0.35);
    overflow: hidden;
  }
  .card--front { left: 50px; }
  .card--back { left: 630px; }

  .brand {
    position: absolute;
    left: 0; right: 0;
    display: flex;
    align-items: center;
    justify-content: center;
    gap: 10px;
  }
  .brand__dot {
    width: 22px; height: 22px;
    border-radius: 50%;
    background: var(--blue);
  }
  .brand__name {
    font-weight: 900;
    font-size: 38px;
    letter-spacing: 2px;
    color: var(--blue);
  }
  .card--front .brand { top: 42px; }
  .card--back .brand { top: 100px; }
  .card--back .brand__name { font-size: 46px; }
  .card--back .brand__dot { width: 26px; height: 26px; }

  .person {
    position: absolute;
    top: 112px; left: 0; right: 0;
    text-align: center;
  }
  .person__name {
    font-size: 22px;
    font-weight: 700;
    color: var(--blue);
  }
  .person__name .surname { color: var(--purple); }
  .person__role {
    font-size: 10px;
    letter-spacing: 0.5px;
    color: var(--ink);
    margin-top: 2px;
  }

  .contact-band {
    position: absolute;
    top: 172px; left: 0;
    width: 100%;
    height: 96px;
    background: var(--blue);
    display: flex;
  }
  .contact-band__cell {
    flex: 1;
    display: flex;
    flex-direction: column;
    align-items: center;
    justify-content: center;
    gap: 10px;
    color: var(--white);
    font-size: 13px;
  }
  .contact-band__cell + .contact-band__cell { border-left: 2px solid var(--white); }
  .contact-band__icon { width: 36px; height: 36px; }

  .web-line {
    position: absolute;
    top: 192px; left: 0; right: 0;
    display: flex;
    justify-content: center;
    align-items: center;
    gap: 8px;
    font-size: 15px;
    color: var(--ink);
  }
  .web-line svg { width: 14px; height: 14px; }
  .back-stripe {
    position: absolute;
    bottom: 0; left: 0;
    width: 100%;
    height: 12px;
    background: var(--blue);
  }
</style>
</head>
<body>
  <section class="card card--front">
    <div class="brand">
      <span class="brand__dot"></span>
      <span class="brand__name">SWIFTWAY</span>
    </div>
    <div class="person">
      <div class="person__name">Daria <span class="surname">Okonkwo</span></div>
      <div class="person__role">DIRECTOR / OWNER</div>
    </div>
    <div class="contact-band">
      <div class="contact-band__cell">
        <svg class="contact-band__icon" viewBox="0 0 36 36" fill="none" stroke="#fff" stroke-width="2">
          <circle cx="18" cy="18" r="16"/>
          <rect x="10" y="12" width="16" height="12"/>
          <path d="M10 12 L18 19 L26 12"/>
        </svg>
        <span>info@swiftway.co.za</span>
      </div>
      <div class="contact-band__cell">
        <svg class="contact-band__icon" viewBox="0 0 36 36" fill="none" stroke="#fff" stroke-width="2">
          <circle cx="18" cy="18" r="16"/>
          <rect x="13" y="9" width="10" height="18" rx="1.5"/>
          <line x1="16" y1="24" x2="20" y2="24"/>
        </svg>
        <span>071 555 01234</span>
      </div>
      <div class="contact-band__cell">
        <svg class="contact-band__icon" viewBox="0 0 36 36" fill="none" stroke="#fff" stroke-width="2">
          <circle cx="18" cy="18" r="16"/>
          <rect x="11" y="12" width="14" height="9"/>
          <line x1="8" y1="24" x2="28" y2="24"/>
        </svg>
        <span>www.swiftway.co.za</span>
      </div>
    </div>
  </section>

  <section class="card card--back">
    <div class="brand">
      <span class="brand__dot"></span>
      <span class="brand__name">SWIFTWAY</span>
    </div>
    <div class="web-line">
      <svg viewBox="0 0 14 14" fill="none" stroke="#333" stroke-width="1.2">
        <circle cx="7" cy="7" r="6"/>
        <path d="M4 5 L10 7 L4 9 L5.5 7 Z" fill="#333"/>
      </svg>
      <span>www.swiftway.co.za</span>
    </div>
    <div class="back-stripe"></div>
  </section>
</body>
</html>
```